2013 Golf Outing Flyer

Our charitable organization was created in honor of my daughter who died at age 16. Our annual fundraiser is a golf tournament. I am not a creative person so I'd like someone to design a printable flyer that grabs people's attention but is not too busy while incorportating our organization's logo with the basic information.

Event details:
3rd Annual Marissa Joan Caldwell Memorial Golf Tournament
4 person scramble

Saturday October 5th, 2013
Larkspur Golf Club, Auburn, IL
9:30 Registration
Shotgun start at noon
To Register go online to www.marissajcaldwellgolf.teesignups.example or email
marissacaldwellfund@mailbox.example

Scholarships to Cedar Rapids Hollow High School seniors are made possible by our orgnization through this fundraiser.
Updates

Target Market(s)

golfers and businesses willing to sponsor event

Industry/Entity Type

School

Requirements
Must have
• single page-easy to print
includes non profit organization logo which I attached (think I did)
Specific information about the tournament- date and location and registration info
Nice to have
• company logo and the golf outing logo but if both are too much, then just the golf logo and the organization name can be at the bottom

```html
<!DOCTYPE html>
<html lang="en">
<head>
<meta charset="utf-8">
<title>3rd Annual Marissa Joan Caldwell Memorial Golf Tournament</title>
<link rel="stylesheet" href="https://fonts.googleapis.com/css2?family=Source+Sans+3:wght@400&display=swap">
<style>
  :root {
    --panel: #e6e7e8;
    --panel-edge: #8c8e91;
    --purple: #6b3a92;
    --red: #e3222b;
    --deep-red: #c1272d;
    --brown: #5b3d20;
    --blue: #2a78bd;
    --sky: #9cc3e4;
    --grass: #4f8c2f;
    --trees: #3f5a2a;
    --badge-light: #f2f2f2;
    --badge-dark: #b8b9bb;
  }
  html, body {
    margin: 0;
    padding: 0;
    width: 900px;
    height: 1200px;
    overflow: hidden;
    background: #ffffff;
  }
  .flyer {
    position: relative;
    width: 900px;
    height: 1200px;
    overflow: hidden;
    font-family: "Source Sans 3", "Myriad Pro", Arial, sans-serif;
  }
  .course-photo {
    position: absolute;
    inset: 0;
    background:
      linear-gradient(180deg, var(--sky) 0%, #c9ddef 30%, var(--trees) 38%, #557a34 52%, var(--grass) 64%, #3d7a27 100%);
  }
  .panels {
    position: absolute;
    inset: 0;
  }
  .text {
    position: absolute;
    margin: 0;
    white-space: nowrap;
    font-weight: 400;
    line-height: 1;
  }
  .title-annual { left: 33px; top: 70px; font-size: 36px; color: var(--purple); }
  .title-name { left: 33px; top: 120px; font-size: 37px; color: var(--red); line-height: 48px; }
  .title-format { left: 33px; top: 232px; font-size: 38px; color: var(--brown); }

  .badge-name {
    position: absolute;
    left: 502px;
    top: 2px;
    width: 256px;
    height: 190px;
    display: flex;
    align-items: center;
    justify-content: center;
    text-align: center;
    font-size: 24px;
    line-height: 1.15;
    color: var(--brown);
  }

  .details { position: absolute; left: 266px; top: 456px; }
  .details-heading { font-size: 32px; color: var(--deep-red); margin: 0 0 14px; line-height: 36px; }
  .details-row { display: flex; font-size: 32px; line-height: 48px; }
  .details-label { width: 120px; color: var(--deep-red); }
  .details-value { color: var(--blue); }
  .details-time { padding-left: 4px; }
  .details-time span { display: block; }
  .details-time .gap { display: inline-block; width: 22px; }

  .register-label { font-size: 32px; color: var(--deep-red); }
  .register-url { font-size: 30px; color: var(--blue); }
  .r1 { left: 220px; top: 945px; }
  .r2 { left: 190px; top: 988px; }
  .r3 { left: 160px; top: 1033px; }
  .r4 { left: 133px; top: 1075px; }

  .footnote {
    position: absolute;
    left: 117px;
    top: 1136px;
    margin: 0;
    font-size: 20px;
    line-height: 28px;
    color: var(--red);
  }
</style>
</head>
<body>
<main class="flyer">
  <div class="course-photo" role="img" aria-label="Photo of a golf course fairway with trees, sand bunkers and a blue sky with clouds"></div>

  <svg class="panels" width="900" height="1200" viewBox="0 0 900 1200" aria-hidden="true">
    <defs>
      <radialGradient id="badgeFill" cx="40%" cy="35%" r="70%">
        <stop offset="0" stop-color="var(--badge-light)"/>
        <stop offset="1" stop-color="var(--badge-dark)"/>
      </radialGradient>
    </defs>
    <!-- header panel -->
    <polygon points="0,0 900,0 900,10 632,310 0,310" fill="var(--panel-edge)"/>
    <polygon points="0,0 900,0 620,296 0,296" fill="var(--panel)"/>
    <!-- badge -->
    <ellipse cx="630" cy="97" rx="128" ry="95" fill="url(#badgeFill)"/>
    <!-- details panel -->
    <rect x="220" y="450" width="680" height="260" fill="var(--panel-edge)"/>
    <rect x="233" y="437" width="667" height="262" fill="var(--panel)"/>
    <!-- footer panel -->
    <polygon points="178,912 900,912 900,1200 0,1200 0,1128" fill="var(--panel-edge)"/>
    <polygon points="192,926 900,926 900,1200 0,1200 0,1160" fill="var(--panel)"/>
  </svg>

  <h1 class="text title-annual">3rd Annual</h1>
  <p class="text title-name">Marissa Joan Caldwell<br>Memorial Golf Tournament</p>
  <p class="text title-format">4 person scramble</p>

  <div class="badge-name">MJC<br>Memorial Golf Outing</div>

  <section class="details">
    <h2 class="details-heading">Event&nbsp; Details</h2>
    <div class="details-row"><span class="details-label">place :</span><span class="details-value">Larkspur Golf Club, Auburn, IL</span></div>
    <div class="details-row"><span class="details-label">Date&nbsp; :</span><span class="details-value">Saturday October 5th, 2013</span></div>
    <div class="details-row"><span class="details-label">Time&nbsp; :</span><span class="details-value details-time"><span>9:30<i class="gap"></i>Registration</span><span>Shotgun start at noon</span></span></div>
  </section>

  <p class="text register-label r1">Register online at</p>
  <p class="text register-url r2">www.marissajcaldwellgolf.teesignups.example</p>
  <p class="text register-label r3">or email at</p>
  <p class="text register-url r4">marissacaldwellfund@mailbox.example</p>

  <p class="footnote">Scholarships to Cedar Rapids Hollow High School seniors are made possible<br>by our orgnization through this fundraise</p>
</main>
</body>
</html>
```